Tivo shoes is a wholesale shoe sales company , mostly working in female shoes and kiddies shoes with a small mens section . looking for a clean slick look. http://www.brindafeet.co.za/shop/ is a good reference

It Company

```html
<!DOCTYPE html>
<html lang="en">
<head>
<meta charset="utf-8">
<title>Lunelle Shoes</title>
<link href="https://fonts.googleapis.com/css2?family=Jost:wght@400;500;600&family=Great+Vibes&family=Cormorant+Garamond:wght@400&display=swap" rel="stylesheet">
<style>
  :root {
    --page-grey: #e3e3e3;
    --sheet: #ffffff;
    --navy: #283170;
    --ink: #1e1e1e;
    --muted: #555555;
    --box-grey: #a9a9a9;
    --divider: #b9b9b9;
    --hero-light: #eef2f4;
    --hero-mid: #e2e8ec;
    --script-grey: #5e5e5e;
  }
  * { box-sizing: border-box; margin: 0; padding: 0; }
  html, body { width: 1200px; height: 900px; overflow: hidden; }
  body {
    background: var(--page-grey);
    font-family: "Jost", sans-serif;
    position: relative;
  }
  .sheet {
    position: absolute; left: 65px; top: 0;
    width: 1070px; height: 685px;
    background: var(--sheet);
  }
  .brand {
    position: absolute; left: 150px; top: 62px;
    font-size: 42px; font-weight: 500; color: var(--navy);
    letter-spacing: 1px; line-height: 1;
  }
  .account-links {
    position: absolute; right: 40px; top: 113px;
    display: flex; gap: 64px; list-style: none;
  }
  .account-links a {
    color: var(--navy); text-decoration: none;
    font-size: 18px; letter-spacing: 3px;
  }
  .main-nav {
    position: absolute; left: 58px; right: 54px; top: 172px;
    display: flex; justify-content: space-between; list-style: none;
  }
  .main-nav a {
    color: var(--ink); text-decoration: none;
    font-size: 18px; letter-spacing: 4.5px;
  }
  .hero {
    position: absolute; left: 44px; top: 244px;
    width: 992px; height: 404px;
    background: linear-gradient(180deg, var(--hero-light) 0%, var(--hero-mid) 85%, #f4f6f7 100%);
    overflow: hidden;
  }
  .hero-photo {
    position: absolute; right: 0; top: 0;
    width: 470px; height: 404px;
    background: radial-gradient(ellipse at 70% 50%, #c9d0d8 0%, #dde3e8 45%, rgba(226,232,236,0) 75%);
  }
  .hero-title {
    position: absolute; left: 78px; top: 146px;
    font-family: "Great Vibes", cursive;
    font-size: 60px; color: var(--script-grey); line-height: 1;
  }
  .hero-sub {
    position: absolute; left: 120px; top: 204px;
    font-family: "Cormorant Garamond", serif;
    font-size: 27px; letter-spacing: 2px; color: var(--script-grey);
  }
  .promo-band {
    position: absolute; left: 65px; top: 685px;
    width: 1070px; height: 122px;
    background: var(--page-grey);
    display: flex;
  }
  .promo { position: relative; text-align: center; padding-top: 10px; }
  .promo + .promo::before {
    content: ""; position: absolute; left: 0; top: 7px;
    width: 2px; height: 100px; background: var(--divider);
  }
  .promo-1 { width: 331px; }
  .promo-2 { width: 406px; }
  .promo-3 { width: 333px; }
  .promo h2 {
    font-weight: 400; font-size: 28px; letter-spacing: 6px;
    color: var(--ink); line-height: 1.2;
  }
  .promo-box {
    height: 42px; line-height: 42px;
    background: var(--box-grey); color: #fff;
    font-size: 17px; text-align: center;
  }
  .promo-1 .promo-box { position: absolute; left: 31px; top: 51px; width: 278px; }
  .promo-2 .promo-box { position: absolute; left: 66px; top: 51px; width: 278px; }
  .promo-box strong { font-weight: 500; }
  .newsletter {
    position: absolute; left: 22px; top: 51px; display: flex; gap: 8px;
  }
  .newsletter .promo-box { width: 223px; }
  .subscribe {
    width: 47px; height: 42px; background: var(--box-grey);
    display: flex; align-items: center; justify-content: center;
  }
  .site-footer {
    position: absolute; left: 65px; top: 807px;
    width: 1070px; height: 93px; background: var(--sheet);
    font-size: 17px; line-height: 25px;
  }
  .footer-address {
    position: absolute; left: 31px; top: 10px;
    color: var(--muted); font-style: normal;
  }
  .footer-links { position: absolute; left: 365px; top: 10px; list-style: none; }
  .footer-links a { color: var(--navy); text-decoration: none; }
</style>
</head>
<body>
  <header class="sheet">
    <div class="brand">Lunelle shoes</div>
    <ul class="account-links">
      <li><a href="#">Account</a></li>
      <li><a href="#">Cart</a></li>
      <li><a href="#">Checkout</a></li>
      <li><a href="#">Log In</a></li>
    </ul>
    <ul class="main-nav">
      <li><a href="#">LADIES</a></li>
      <li><a href="#">MENS</a></li>
      <li><a href="#">GIRLS</a></li>
      <li><a href="#">BOYS</a></li>
      <li><a href="#">ABOUT US</a></li>
      <li><a href="#">CONTACT</a></li>
      <li><a href="#">FAQ</a></li>
    </ul>
    <section class="hero">
      <div class="hero-photo" role="img" aria-label="Woman in a striped dress running while pulling a flock of boots and heels on strings"></div>
      <p class="hero-title">Summer Specials</p>
      <p class="hero-sub">up to 40% off&nbsp; select styles</p>
    </section>
  </header>

  <section class="promo-band">
    <div class="promo promo-1">
      <h2>MY CART</h2>
      <div class="promo-box">There are <strong>2 items</strong> in your cart.</div>
    </div>
    <div class="promo promo-2">
      <h2>CLEARANCE</h2>
      <div class="promo-box">Out of season and clearance items.</div>
    </div>
    <div class="promo promo-3">
      <h2>NEWSLETTER</h2>
      <div class="newsletter">
        <div class="promo-box">Enter your email to subscribe.</div>
        <div class="subscribe">
          <svg width="24" height="28" viewBox="0 0 24 28" aria-hidden="true">
            <polyline points="5,2 18,14 5,26" fill="none" stroke="#ffffff" stroke-width="6"/>
          </svg>
        </div>
      </div>
    </div>
  </section>

  <footer class="site-footer">
    <address class="footer-address">Lunelle Shoes<br>123 Main Street<br>City, State, Country</address>
    <ul class="footer-links">
      <li><a href="#">Terms and Conditions</a></li>
      <li><a href="#">Privacy Policy</a></li>
      <li><a href="#">Orders and Returns</a></li>
    </ul>
  </footer>
</body>
</html>
```